I need a professional business card to handout at networking events for my senior helper business. I would like to use the logo I have uploaded. The design should be clear and easy to read and should list the following information...
Dessa Quillan
Owner
www.BrightwayElderAssist.example
Quillport, Nevada
555.304.2291
Dessa@brightwayelderassist.example

Target Market(s)

Senior Citizens

Industry/Entity Type

Personal Helper/ Assisstant

Contact Information for Business Card

I have included the details in the project description box.

Font styles to use
Serif

Colors
0054AA
0677BA
7BADD7
CADEEF
E8F1F8
59FF00
82FF00
B8FF75
E3FFCB
F4FFEA
E54698
E96AAD
F1A4CE
F9D9EA
FCEFF6
6B429C
8869AF
B7A5CE
E3DAEB
F3F0F8

Requirements
Must have
• Include uploaded logo
Nice to have
• The log that has been uploaded
Should not have
• No crazy fonts

```html
<!DOCTYPE html>
<html lang="en">
<head>
<meta charset="utf-8">
<title>Brightway Elder Assist – Business Card</title>
<link rel="stylesheet" href="https://fonts.googleapis.com/css2?family=Montserrat:wght@800&family=Open+Sans:wght@400;600&display=swap">
<style>
  :root {
    --stage: #232325;
    --card: #232328;
    --card-shade: #1d1d21;
    --card-deep: #19191c;
    --teal: #1a9a9c;
    --pink: #e0195f;
    --violet: #6b52b8;
    --ink-light: #ffffff;
    --emboss: #16161a;
  }
  * { margin: 0; padding: 0; box-sizing: border-box; }
  html, body { width: 1200px; height: 779px; overflow: hidden; background: var(--stage); }
  .stage {
    position: relative; width: 1200px; height: 779px;
    display: flex; justify-content: center; align-items: center; gap: 90px;
  }
  .card {
    position: relative; width: 300px; height: 525px;
    border-radius: 22px; background: var(--card); overflow: hidden;
    box-shadow: 0 14px 30px rgba(0,0,0,.55);
    font-family: "Open Sans", sans-serif;
  }
  /* back */
  .card-back .brand-mark {
    position: absolute; left: 50%; top: 50%;
    transform: translate(-50%, -50%) rotate(-90deg);
    display: flex; align-items: center; gap: 16px; white-space: nowrap;
  }
  .card-back .brand-dot { width: 46px; height: 46px; border-radius: 50%; background: var(--emboss); }
  .card-back .brand-name { font-size: 38px; font-weight: 400; color: var(--emboss); letter-spacing: 1px; }
  /* front */
  .front-logo {
    position: absolute; top: 36px; left: 0; right: 0;
    display: flex; justify-content: center; align-items: center; gap: 8px;
  }
  .front-logo .brand-dot { width: 18px; height: 18px; border-radius: 50%; background: var(--violet); }
  .front-logo .brand-name { font-size: 21px; color: var(--violet); font-weight: 400; }
  .curves { position: absolute; left: 0; bottom: 0; width: 300px; height: 260px; }
  .identity { position: absolute; top: 168px; left: 0; right: 0; text-align: center; color: var(--ink-light); }
  .person-name { font-family: "Montserrat", sans-serif; font-weight: 800; font-size: 24px; }
  .person-name .first { color: var(--teal); }
  .person-name .last { color: var(--pink); }
  .role { font-size: 13px; font-weight: 600; margin-top: 2px; }
  .icons { display: flex; justify-content: center; gap: 7px; margin: 9px 0 6px; }
  .icon { width: 22px; height: 22px; border-radius: 50%; background: var(--pink); display: flex; align-items: center; justify-content: center; }
  .contact { font-size: 12.5px; line-height: 1.45; }
  .location { position: absolute; bottom: 40px; left: 0; right: 0; text-align: center; color: var(--ink-light); font-size: 14px; }
  .location .icon { margin: 0 auto 6px; }
</style>
</head>
<body>
<main class="stage">
  <section class="card card-back" aria-label="Card back">
    <div class="brand-mark">
      <span class="brand-dot"></span>
      <span class="brand-name">Brightway Elder Assist</span>
    </div>
  </section>

  <section class="card card-front" aria-label="Card front">
    <div class="front-logo">
      <span class="brand-dot"></span>
      <span class="brand-name">Brightway Elder Assist</span>
    </div>

    <svg class="curves" viewBox="0 0 300 260" aria-hidden="true">
      <path d="M0 70 Q140 150 300 20 L300 260 L0 260 Z" fill="var(--card-shade)"/>
      <path d="M80 260 Q180 160 300 110 L300 260 Z" fill="var(--card-deep)"/>
    </svg>

    <div class="identity">
      <div class="person-name"><span class="first">Dessa</span> <span class="last">Quillan</span></div>
      <div class="role">Owner</div>
      <div class="icons">
        <span class="icon"><svg width="12" height="12" viewBox="0 0 24 24"><path fill="#fff" d="M6.6 10.8a15 15 0 0 0 6.6 6.6l2.2-2.2a1 1 0 0 1 1-.25 11.4 11.4 0 0 0 3.6.57 1 1 0 0 1 1 1V20a1 1 0 0 1-1 1A17 17 0 0 1 3 4a1 1 0 0 1 1-1h3.5a1 1 0 0 1 1 1c0 1.250.2 2.45.57 3.57a1 1 0 0 1-.25 1z"/></svg></span>
        <span class="icon"><svg width="12" height="12" viewBox="0 0 24 24"><path fill="#fff" d="M3 6h18v12H3z"/><path d="M3 6l9 7 9-7" stroke="#e0195f" stroke-width="2" fill="none"/></svg></span>
        <span class="icon"><svg width="12" height="12" viewBox="0 0 24 24"><circle cx="12" cy="12" r="9" fill="none" stroke="#fff" stroke-width="2"/><path d="M3 12h18M12 3c3 3 3 15 0 18M12 3c-3 3-3 15 0 18" stroke="#fff" stroke-width="1.6" fill="none"/></svg></span>
      </div>
      <div class="contact">
        <div>555.304.2291</div>
        <div>www.BrightwayElderAssist.example</div>
        <div>Dessa@brightwayelderassist.example</div>
      </div>
    </div>

    <div class="location">
      <span class="icon"><svg width="12" height="12" viewBox="0 0 24 24"><path fill="#fff" d="M12 2a7 7 0 0 0-7 7c0 5 7 13 7 13s7-8 7-13a7 7 0 0 0-7-7zm0 9.5A2.5 2.5 0 1 1 12 6.5a2.5 2.5 0 0 1 0 5z"/></svg></span>
      <div>Quillport, Nevada</div>
    </div>
  </section>
</main>
</body>
</html>
```